Can you make our site AWESOME?

Hi Guys,

I am a co-founder of Tipper Crate Rentals Australia, the world's first e-commerce skip bin business.

We are looking to update our site before a launch into the UK in March.

Please help us by submitting your designs for the following pages:

- Home page (www.tippercraterentals-example.com.au)
- About us (https://www.tippercraterentals-example.com.au/pages/about-us
- Contact us (https://www.tippercraterentals-example.com.au/pages/contact-us)
- Quick Quote / Pricing (https://www.tippercraterentals-example.com.au/pages/free-instant-quote-skip-bin-hire)

NOTES:
- Design should be high-converting
- best designs will be fresh, modern, easy to read, distinctive and memorable
- please use our logo and video colours
- feel free to change logos, layout, images and anything else you feel can be improved
- the winning designer will potentially have the opportunity to re-design the other pages on our site
- brief is for design only

Any questions just ask.

Thanks,
Oliver

```html
<!DOCTYPE html>
<html lang="en">
<head>
<meta charset="utf-8">
<title>Tipper Crate Rentals Australia – Home Page Concepts</title>
<link href="https://fonts.googleapis.com/css2?family=Montserrat:wght@500;600;700&family=Open+Sans:wght@400;600&display=swap" rel="stylesheet">
<style>
:root{
  --stage:#f3f3f5;
  --navy:#1f2350;
  --green:#2f9e3f;
  --lilac:#f2f1f7;
  --text:#333;
  --muted:#888;
  --black:#141414;
}
*{box-sizing:border-box;margin:0;padding:0}
html,body{width:890px;height:1200px;overflow:hidden}
body{background:var(--stage);font-family:"Open Sans",sans-serif;color:var(--text);position:relative}
.page{position:absolute;top:82px;width:317px;height:1036px;background:#fff;box-shadow:0 2px 10px rgba(0,0,0,.12);display:flex;flex-direction:column;overflow:hidden}
.page--earth{left:88px}
.page--bins{left:484px}
.site-header{height:29px;display:flex;align-items:center;justify-content:space-between;padding:0 28px 0 30px;background:#fff}
.brand{display:flex;align-items:center;gap:4px;font-family:"Montserrat",sans-serif;font-weight:700;font-size:5.6px;color:var(--navy);line-height:1.25;white-space:nowrap}
.brand-mark{width:9px;height:9px;background:var(--navy);border-radius:50%;flex:none}
.header-right{display:flex;flex-direction:column;align-items:flex-end;gap:5px}
.util{display:flex;align-items:center;gap:4px;font-size:4.4px;font-weight:600;font-family:"Montserrat",sans-serif;color:var(--navy)}
.util .login{border:1px solid var(--green);color:var(--green);border-radius:6px;padding:1px 4px}
.util .cart{width:10px;height:10px;border-radius:50%;background:var(--green);display:flex;align-items:center;justify-content:center}
.nav{display:flex;gap:7px;font-family:"Montserrat",sans-serif;font-size:4.3px;font-weight:600;color:var(--navy);margin-right:-6px}
.nav .active{color:var(--green)}
.hero{height:154px;position:relative;color:#fff;text-align:center;font-family:"Montserrat",sans-serif}
.hero-art{position:absolute;inset:0}
.page--earth .hero-art{background:linear-gradient(160deg,#4a3a2c 0%,#23344f 100%)}
.page--bins .hero-art{background:linear-gradient(180deg,#4f7aa3 0%,#8a4a3c 100%)}
.hero-inner{position:relative;display:flex;flex-direction:column;align-items:center}
.page--earth .hero-inner{padding-top:37px}
.page--bins .hero-inner{padding-top:19px}
.hero h1{font-size:10.6px;font-weight:700;letter-spacing:.2px}
.hero .tag{font-family:"Open Sans",sans-serif;font-size:6px;margin-top:5px}
.search{display:flex;width:176px;height:14px;margin:10px 0}
.search .field{flex:1;background:#fff;color:#999;font-family:"Open Sans",sans-serif;font-size:4px;display:flex;align-items:center;gap:2px;padding-left:5px}
.search .btn{width:34px;background:var(--green);color:#fff;font-family:"Montserrat",sans-serif;font-size:4.2px;font-weight:700;display:flex;align-items:center;justify-content:center;gap:2px}
.hero .call{font-size:7.8px;font-weight:700}
.stars{color:#ffd400;font-size:7px;letter-spacing:1px;margin-top:2px}
.arrow{position:absolute;top:74px}
.arrow.l{left:12px}.arrow.r{right:12px}
h2{font-family:"Montserrat",sans-serif;font-weight:600;font-size:9.6px;color:var(--navy);text-align:center}
.welcome{height:191px;padding-top:28px;display:flex;flex-direction:column;align-items:center}
.welcome .sub{font-size:4.8px;margin-top:6px}
.video{width:156px;height:97px;margin-top:12px;background:linear-gradient(180deg,#8284d2 0%,#6d78a8 100%);position:relative;display:flex;align-items:center;justify-content:center}
.video .play{width:18px;height:18px;border-radius:50%;background:#222;display:flex;align-items:center;justify-content:center}
.how{height:168px;background:var(--lilac);padding-top:25px;display:flex;flex-direction:column;align-items:center}
.steps{display:flex;align-items:flex-start;margin-top:12px}
.step{width:80px;text-align:center}
.step .ring{width:32px;height:32px;border-radius:50%;border:1px solid #c9c9d3;background:#fff;margin:0 auto;display:flex;align-items:center;justify-content:center}
.step .ring.on{border-color:var(--green)}
.step h3{font-family:"Montserrat",sans-serif;font-size:5.5px;font-weight:600;color:var(--navy);margin-top:6px;line-height:1.4}
.step.on h3{color:var(--green)}
.step p{font-size:3.5px;color:var(--muted);margin-top:6px;line-height:1.6;padding:0 6px}
.link{width:20px;height:1px;background:#c9c9d3;margin-top:16px;margin-left:-14px;margin-right:-14px;position:relative}
.link.on{background:var(--green)}
.link i{position:absolute;left:7px;top:-2.5px;width:6px;height:6px;border-radius:50%;background:#fff;border:1px solid #c9c9d3}
.link.on i{border-color:var(--green)}
.cta{margin-top:13px;background:var(--green);color:#fff;font-family:"Montserrat",sans-serif;font-size:4.4px;font-weight:700;border-radius:8px;padding:5px 9px}
.save{height:151px;padding-top:25px}
.perks{display:flex;justify-content:center;gap:1px;margin-top:14px}
.perk{width:66px;height:70px;text-align:center;padding-top:8px}
.perk.on{box-shadow:0 1px 5px rgba(0,0,0,.12);border-bottom:2px solid var(--green)}
.perk .globe{width:18px;height:18px;border-radius:50%;border:1.3px solid var(--navy);margin:0 auto}
.perk.on .globe{border-color:var(--green)}
.perk h3{font-family:"Montserrat",sans-serif;font-size:5px;font-weight:600;color:var(--navy);margin-top:5px;line-height:1.4}
.perk.on h3{color:var(--green)}
.perk p{font-size:3.4px;color:var(--muted);margin-top:4px;line-height:1.6;padding:0 3px}
.ready{height:113px;background:linear-gradient(90deg,#262a5c,#1f2350 50%,#262a5c);color:#fff;text-align:center;font-family:"Montserrat",sans-serif;padding-top:26px;display:flex;flex-direction:column;align-items:center}
.ready h2{color:#fff}
.ready .sub{font-family:"Open Sans",sans-serif;font-size:4.6px;margin-top:6px}
.ready .search{margin:8px 0 10px}
.ready .call{font-size:7.8px;font-weight:700}
.industries{height:134px;padding-top:27px}
.sectors{display:flex;justify-content:center;gap:5px;margin-top:14px}
.sector{width:48px;text-align:center}
.sector .tile{height:45px;border:1px solid #d5d5dc;border-radius:2px;display:flex;align-items:center;justify-content:center}
.sector span{display:block;font-size:5px;margin-top:6px;font-weight:600;color:#444}
.site-footer{flex:1;background:var(--black);color:#bbb;text-align:center;padding-top:17px;font-size:3.6px;line-height:1}
.social{display:flex;justify-content:center;gap:4px}
.social i{width:12px;height:12px;border-radius:50%;border:1px solid #777;display:block}
.site-footer .line{margin-top:8px}
.site-footer .line+.line{margin-top:5px}
.pay{display:flex;justify-content:center;gap:7px;margin-top:10px}
.pay i{width:14px;height:8px;background:#666;border-radius:1px;display:block}
.pay i.wide{width:26px}
</style>
</head>
<body>

<section class="page page--earth">
  <header class="site-header">
    <div class="brand"><span class="brand-mark"></span><span>TIPPER CRATE RENTALS<br>AUSTRALIA</span></div>
    <div class="header-right">
      <div class="util">
        <svg width="5" height="5" viewBox="0 0 10 10"><path d="M2 1l2 2-1 1.5a6 6 0 003 3L7.5 6l2 2-1.5 1.5C4 9 1 6 .5 2z" fill="#2f9e3f"/></svg>
        CALL NOW: 1800 000 123 <span class="login">LOGIN</span>
        <span class="cart"><svg width="5" height="5" viewBox="0 0 10 10"><path d="M1 2h2l1 5h5l1-4H4" stroke="#fff" fill="none"/></svg></span>
      </div>
      <nav class="nav"><span class="active">PRICING</span><span>LEARN MORE</span><span>ABOUT</span><span>TRADE SECRETS</span><span>CONTACT</span></nav>
    </div>
  </header>
  <div class="hero">
    <div class="hero-art" role="img" aria-label="Photo of the Earth from space at night with glowing connection lines"></div>
    <svg class="arrow l" width="6" height="10" viewBox="0 0 6 10"><path d="M5 1L1 5l4 4" stroke="#fff" fill="none" stroke-width="1.2"/></svg>
    <svg class="arrow r" width="6" height="10" viewBox="0 0 6 10"><path d="M1 1l4 4-4 4" stroke="#fff" fill="none" stroke-width="1.2"/></svg>
    <div class="hero-inner">
      <h1>1000'S OF SKIPS AT YOUR FINGER TIPS</h1>
      <p class="tag">Best Service &amp; Price | Hassle Free | Australia Wide</p>
      <div class="search"><div class="field"><svg width="3" height="4" viewBox="0 0 6 8"><path d="M3 8S0 4.5 0 3a3 3 0 016 0c0 1.5-3 5-3 5z" fill="#999"/></svg>Enter Postcode or suburb</div><div class="btn"><svg width="4" height="4" viewBox="0 0 8 8"><circle cx="3.2" cy="3.2" r="2.3" stroke="#fff" fill="none"/><path d="M5 5l2.5 2.5" stroke="#fff"/></svg>SEARCH</div></div>
      <p class="call">CALL NOW: 1800 000 123</p>
      <div class="stars">★★★★★</div>
    </div>
  </div>
  <section class="welcome">
    <h2>WELCOME TO TIPPER CRATE RENTALS AUSTRALIA</h2>
    <p class="sub">Australia's Highest Rated Skip Bin Hire Company - Rated by You</p>
    <div class="video" role="img" aria-label="Explainer video still: cartoon homeowner in front of a house with TCR Australia title">
      <span class="play"><svg width="7" height="7" viewBox="0 0 10 10"><path d="M2 1l7 4-7 4z" fill="#fff"/></svg></span>
    </div>
  </section>
  <section class="how">
    <h2>HOW IT WORKS</h2>
    <div class="steps">
      <div class="step on"><div class="ring on"><svg width="14" height="12" viewBox="0 0 14 12"><rect x="1" y="1" width="12" height="8" fill="none" stroke="#2f9e3f"/><path d="M5 11h4" stroke="#2f9e3f"/></svg></div><h3>Simple,<br>Easy Booking</h3><p>Call 1800 000 123 or click here to get started with your instant quote</p></div>
      <div class="link on"><i></i></div>
      <div class="step"><div class="ring"><svg width="12" height="10" viewBox="0 0 12 10"><rect width="12" height="10" fill="#1f2350"/><path d="M0 0l6 5 6-5" stroke="#fff" fill="none"/></svg></div><h3>Instant<br>Confirmation</h3><p>Receive your booking details and a 30 minute courtesy call before drop off</p></div>
      <div class="link"><i></i></div>
      <div class="step"><div class="ring"><svg width="12" height="12" viewBox="0 0 12 12"><path d="M1 2h10l-2 9H3z" fill="#1f2350"/></svg></div><h3>Gone When<br>Your Ready!</h3><p>Let us know and your bin will be gone within 24hrs</p></div>
    </div>
    <span class="cta">GET STARTED</span>
  </section>
  <section class="save">
    <h2>SAVE TIME. SAVE MONEY</h2>
    <div class="perks">
      <div class="perk"><div class="globe"></div><h3>Any Bin, Anytime,<br>Anywhere</h3><p>We connect you with local companies Australia wide</p></div>
      <div class="perk on"><div class="globe"></div><h3>Service<br>Guaranteed</h3><p>Want to speak to someone when it suits you? We answer the</p></div>
      <div class="perk"><div class="globe"></div><h3>Best<br>Pricing</h3><p>We've done the hard work behind the scenes, so with one</p></div>
      <div class="perk"><div class="globe"></div><h3>First Class<br>Supply Partners</h3><p>Our local supply partners are the best in the business</p></div>
    </div>
  </section>
  <section class="ready" role="img" aria-label="Dark navy band over a photo of skip bins">
    <h2>WE'RE READY TO GO!</h2>
    <p class="sub">To book, ask questions or just for a chat, call us 7 days a week, 7.30am to 8pm</p>
    <div class="search"><div class="field"><svg width="3" height="4" viewBox="0 0 6 8"><path d="M3 8S0 4.5 0 3a3 3 0 016 0c0 1.5-3 5-3 5z" fill="#999"/></svg>Enter Postcode or suburb</div><div class="btn"><svg width="4" height="4" viewBox="0 0 8 8"><circle cx="3.2" cy="3.2" r="2.3" stroke="#fff" fill="none"/><path d="M5 5l2.5 2.5" stroke="#fff"/></svg>SEARCH</div></div>
    <p class="call">CALL NOW: 1800 000 123</p>
  </section>
  <section class="industries">
    <h2>INDUSTRIES WE SERVE</h2>
    <div class="sectors">
      <div class="sector"><div class="tile"><svg width="22" height="20" viewBox="0 0 22 20"><path d="M2 9L11 2l9 7v10H2z" fill="none" stroke="#555"/></svg></div><span>Renovator</span></div>
      <div class="sector"><div class="tile"><svg width="22" height="20" viewBox="0 0 22 20"><path d="M3 17L17 3M5 3l14 14" stroke="#555" stroke-width="1.5"/></svg></div><span>Tradie</span></div>
      <div class="sector"><div class="tile"><svg width="22" height="20" viewBox="0 0 22 20"><rect x="2" y="11" width="10" height="8" fill="#2f9e3f"/><circle cx="16" cy="5" r="2.5" fill="#2f9e3f"/><path d="M16 8v7" stroke="#2f9e3f" stroke-width="3"/></svg></div><span>Builder</span></div>
      <div class="sector"><div class="tile"><svg width="22" height="20" viewBox="0 0 22 20"><path d="M4 19V9h5V2h4v17M13 19h6V11h-6" fill="none" stroke="#555"/></svg></div><span>Corporate</span></div>
      <div class="sector"><div class="tile"><svg width="22" height="20" viewBox="0 0 22 20"><circle cx="11" cy="4" r="2.5" fill="none" stroke="#555"/><path d="M11 7v5M5 12h12M5 12v4M17 12v4M11 12v4" stroke="#555"/></svg></div><span>National</span></div>
    </div>
  </section>
  <footer class="site-footer">
    <div class="social"><i></i><i></i><i></i></div>
    <p class="line">12 Harbour Lane, Sampletown NSW 2000 &nbsp;|&nbsp; 1800 000 123 &nbsp;|&nbsp; info@tippercraterentals-example.com.au</p>
    <p class="line">Waste Types | Skip Bin Sizes | Refund Policy | Pay Later with FlexiPay | FAQ | Privacy</p>
    <p class="line">Tipper Crate Rentals Australia © 2019 All rights reserved.</p>
    <div class="pay"><i></i><i></i><i></i><i></i><i class="wide"></i></div>
  </footer>
</section>

<section class="page page--bins">
  <header class="site-header">
    <div class="brand"><span class="brand-mark"></span><span>TIPPER CRATE RENTALS<br>AUSTRALIA</span></div>
    <div class="header-right">
      <div class="util">
        <svg width="5" height="5" viewBox="0 0 10 10"><path d="M2 1l2 2-1 1.5a6 6 0 003 3L7.5 6l2 2-1.5 1.5C4 9 1 6 .5 2z" fill="#2f9e3f"/></svg>
        CALL NOW: 1800 000 123 <span class="login">LOGIN</span>
        <span class="cart"><svg width="5" height="5" viewBox="0 0 10 10"><path d="M1 2h2l1 5h5l1-4H4" stroke="#fff" fill="none"/></svg></span>
      </div>
      <nav class="nav"><span class="active">PRICING</span><span>LEARN MORE</span><span>ABOUT</span><span>TRADE SECRETS</span><span>CONTACT</span></nav>
    </div>
  </header>
  <div class="hero">
    <div class="hero-art" role="img" aria-label="Photo of open red and green skip bins on grass under a blue sky"></div>
    <svg class="arrow l" width="6" height="10" viewBox="0 0 6 10"><path d="M5 1L1 5l4 4" stroke="#fff" fill="none" stroke-width="1.2"/></svg>
    <svg class="arrow r" width="6" height="10" viewBox="0 0 6 10"><path d="M1 1l4 4-4 4" stroke="#fff" fill="none" stroke-width="1.2"/></svg>
    <div class="hero-inner">
      <h1>1000'S OF SKIPS AT YOUR FINGER TIPS</h1>
      <p class="tag">Best Service &amp; Price | Hassle Free | Australia Wide</p>
      <div class="search"><div class="field"><svg width="3" height="4" viewBox="0 0 6 8"><path d="M3 8S0 4.5 0 3a3 3 0 016 0c0 1.5-3 5-3 5z" fill="#999"/></svg>Enter Postcode or suburb</div><div class="btn"><svg width="4" height="4" viewBox="0 0 8 8"><circle cx="3.2" cy="3.2" r="2.3" stroke="#fff" fill="none"/><path d="M5 5l2.5 2.5" stroke="#fff"/></svg>SEARCH</div></div>
      <p class="call">CALL NOW: 1800 000 123</p>
      <div class="stars">★★★★★</div>
    </div>
  </div>
  <section class="welcome">
    <h2>WELCOME TO TIPPER CRATE RENTALS AUSTRALIA</h2>
    <p class="sub">Australia's Highest Rated Skip Bin Hire Company - Rated by You</p>
    <div class="video" role="img" aria-label="Explainer video still: cartoon homeowner in front of a house with TCR Australia title">
      <span class="play"><svg width="7" height="7" viewBox="0 0 10 10"><path d="M2 1l7 4-7 4z" fill="#fff"/></svg></span>
    </div>
  </section>
  <section class="how">
    <h2>HOW IT WORKS</h2>
    <div class="steps">
      <div class="step on"><div class="ring on"><svg width="14" height="12" viewBox="0 0 14 12"><rect x="1" y="1" width="12" height="8" fill="none" stroke="#2f9e3f"/><path d="M5 11h4" stroke="#2f9e3f"/></svg></div><h3>Simple,<br>Easy Booking</h3><p>Call 1800 000 123 or click here to get started with your instant quote</p></div>
      <div class="link on"><i></i></div>
      <div class="step"><div class="ring"><svg width="12" height="10" viewBox="0 0 12 10"><rect width="12" height="10" fill="#1f2350"/><path d="M0 0l6 5 6-5" stroke="#fff" fill="none"/></svg></div><h3>Instant<br>Confirmation</h3><p>Receive your booking details and a 30 minute courtesy call before drop off</p></div>
      <div class="link"><i></i></div>
      <div class="step"><div class="ring"><svg width="12" height="12" viewBox="0 0 12 12"><path d="M1 2h10l-2 9H3z" fill="#1f2350"/></svg></div><h3>Gone When<br>Your Ready!</h3><p>Let us know and your bin will be gone within 24hrs</p></div>
    </div>
    <span class="cta">GET STARTED</span>
  </section>
  <section class="save">
    <h2>SAVE TIME. SAVE MONEY</h2>
    <div class="perks">
      <div class="perk"><div class="globe"></div><h3>Any Bin, Anytime,<br>Anywhere</h3><p>We connect you with local companies Australia wide</p></div>
      <div class="perk on"><div class="globe"></div><h3>Service<br>Guaranteed</h3><p>Want to speak to someone when it suits you? We answer the</p></div>
      <div class="perk"><div class="globe"></div><h3>Best<br>Pricing</h3><p>We've done the hard work behind the scenes, so with one</p></div>
      <div class="perk"><div class="globe"></div><h3>First Class<br>Supply Partners</h3><p>Our local supply partners are the best in the business</p></div>
    </div>
  </section>
  <section class="ready" role="img" aria-label="Dark navy band over a photo of skip bins">
    <h2>WE'RE READY TO GO!</h2>
    <p class="sub">To book, ask questions or just for a chat, call us 7 days a week, 7.30am to 8pm</p>
    <div class="search"><div class="field"><svg width="3" height="4" viewBox="0 0 6 8"><path d="M3 8S0 4.5 0 3a3 3 0 016 0c0 1.5-3 5-3 5z" fill="#999"/></svg>Enter Postcode or suburb</div><div class="btn"><svg width="4" height="4" viewBox="0 0 8 8"><circle cx="3.2" cy="3.2" r="2.3" stroke="#fff" fill="none"/><path d="M5 5l2.5 2.5" stroke="#fff"/></svg>SEARCH</div></div>
    <p class="call">CALL NOW: 1800 000 123</p>
  </section>
  <section class="industries">
    <h2>INDUSTRIES WE SERVE</h2>
    <div class="sectors">
      <div class="sector"><div class="tile"><svg width="22" height="20" viewBox="0 0 22 20"><path d="M2 9L11 2l9 7v10H2z" fill="none" stroke="#555"/></svg></div><span>Renovator</span></div>
      <div class="sector"><div class="tile"><svg width="22" height="20" viewBox="0 0 22 20"><path d="M3 17L17 3M5 3l14 14" stroke="#555" stroke-width="1.5"/></svg></div><span>Tradie</span></div>
      <div class="sector"><div class="tile"><svg width="22" height="20" viewBox="0 0 22 20"><rect x="2" y="11" width="10" height="8" fill="#2f9e3f"/><circle cx="16" cy="5" r="2.5" fill="#2f9e3f"/><path d="M16 8v7" stroke="#2f9e3f" stroke-width="3"/></svg></div><span>Builder</span></div>
      <div class="sector"><div class="tile"><svg width="22" height="20" viewBox="0 0 22 20"><path d="M4 19V9h5V2h4v17M13 19h6V11h-6" fill="none" stroke="#555"/></svg></div><span>Corporate</span></div>
      <div class="sector"><div class="tile"><svg width="22" height="20" viewBox="0 0 22 20"><circle cx="11" cy="4" r="2.5" fill="none" stroke="#555"/><path d="M11 7v5M5 12h12M5 12v4M17 12v4M11 12v4" stroke="#555"/></svg></div><span>National</span></div>
    </div>
  </section>
  <footer class="site-footer">
    <div class="social"><i></i><i></i><i></i></div>
    <p class="line">12 Harbour Lane, Sampletown NSW 2000 &nbsp;|&nbsp; 1800 000 123 &nbsp;|&nbsp; info@tippercraterentals-example.com.au</p>
    <p class="line">Waste Types | Skip Bin Sizes | Refund Policy | Pay Later with FlexiPay | FAQ | Privacy</p>
    <p class="line">Tipper Crate Rentals Australia © 2019 All rights reserved.</p>
    <div class="pay"><i></i><i></i><i></i><i></i><i class="wide"></i></div>
  </footer>
</section>

</body>
</html>
```